Stationary, Envelopes, Business Cards, Brouchures, Etc Ventisca Home Health
Pediatric Home Health
Stationary, Envelopes, Business Cards, Brouchures, Etc Ventisca Home Health -
Creative Brief
Bright & Fun-filled
Tobias Quillmore
Administrator
4817 Linwood Rd. Suite 318 Brenmoor, Texas 70412 5400 Harlan Pruett Calder Flats, Texas 70588
Brenmoor: 210-555-0147
Calder Flats: 915-555-0182
Mobile: 210-555-0163
Fax: 1-866-555-0129
tobias@myventisca.example
www.myventisca.example
Please keep in mind that we have two locations and would like to include both addresses and phone numbers.
Private Duty Nursing Speech Therapy Physical Therapy Occupational Therapy

```html
<!DOCTYPE html>
<html lang="en">
<head>
<meta charset="utf-8">
<title>Ventisca Home Health – Business Card</title>
<link href="https://fonts.googleapis.com/css2?family=PT+Sans:ital,wght@0,400;0,700;1,400&display=swap" rel="stylesheet">
<style>
  :root {
    --bg: #eee6da;
    --card: #ffffff;
    --orange: #f7a21b;
    --orange-light: #fcc85a;
    --orange-deep: #ee8a10;
    --ink: #2b2b2b;
    --ink-soft: #4a4a4a;
    --blue: #2a8fd6;
    --grey: #777777;
  }
  * { box-sizing: border-box; margin: 0; padding: 0; }
  html, body { width: 1200px; height: 482px; overflow: hidden; }
  body {
    background: var(--bg);
    font-family: "PT Sans", Arial, sans-serif;
    color: var(--ink);
    position: relative;
  }
  .card {
    position: absolute;
    top: 106px;
    width: 526px;
    height: 344px;
    background: var(--card);
    border-radius: 16px;
    overflow: hidden;
    box-shadow: 0 3px 10px rgba(0,0,0,.18);
  }
  .card--front { left: 62px; }
  .card--back { left: 606px; width: 532px; }

  .front__wave { position: absolute; inset: 0; width: 100%; height: 100%; }

  .brand {
    position: absolute;
    top: 26px;
    left: 0;
    right: 0;
    text-align: center;
  }
  .brand__row { display: flex; align-items: center; justify-content: center; gap: 12px; }
  .brand__dot { width: 32px; height: 32px; border-radius: 50%; background: var(--orange); }
  .brand__name { font-size: 34px; font-weight: 700; color: var(--ink); letter-spacing: .3px; }
  .brand__tagline {
    display: inline-block;
    margin-top: 10px;
    padding: 3px 16px;
    border: 1.5px solid var(--blue);
    color: var(--blue);
    font-size: 16px;
    font-style: italic;
  }

  .person { position: absolute; left: 16px; top: 160px; width: 248px; text-align: right; }
  .person__name { font-size: 26px; font-weight: 700; color: var(--ink); line-height: 1; text-align: left; }
  .person__title { font-size: 14px; color: var(--ink); margin-top: 3px; }
  .person__address { font-size: 14px; line-height: 1.3; margin-top: 12px; color: var(--ink); }
  .person__address + .person__address { margin-top: 8px; }

  .divider {
    position: absolute; left: 274px; top: 160px;
    width: 1.5px; height: 166px; background: var(--ink-soft);
  }

  .contacts { position: absolute; left: 286px; top: 170px; list-style: none; }
  .contacts li {
    display: flex; align-items: center; gap: 8px;
    font-size: 14px; height: 27px; color: var(--ink); white-space: nowrap;
  }
  .contacts svg { width: 15px; height: 15px; flex: none; }

  .back__mark {
    position: absolute; left: 24px; top: 56px;
    display: flex; flex-direction: column; align-items: center; gap: 12px;
    width: 220px;
  }
  .back__circle { width: 150px; height: 150px; border-radius: 50%; background: var(--orange); }
  .back__name { font-size: 20px; font-weight: 700; color: var(--ink); white-space: nowrap; }

  .services { position: absolute; left: 296px; top: 94px; list-style: none; }
  .services li {
    display: flex; align-items: center; gap: 8px;
    font-size: 15px; height: 22px; color: var(--ink-soft);
  }
  .services li::before {
    content: ""; width: 11px; height: 11px; background: var(--orange); border-radius: 2px;
  }
  .website {
    position: absolute; left: 0; right: 0; top: 266px;
    text-align: center; font-size: 14px; color: var(--grey);
  }
</style>
</head>
<body>
  <section class="card card--front">
    <svg class="front__wave" viewBox="0 0 526 344" preserveAspectRatio="none" aria-hidden="true">
      <defs>
        <linearGradient id="orangeFill" x1="0" y1="0" x2="0" y2="1">
          <stop offset="0" stop-color="#fcc85a"/>
          <stop offset="0.55" stop-color="#f7a21b"/>
          <stop offset="1" stop-color="#ee8a10"/>
        </linearGradient>
      </defs>
      <path d="M0 128 C120 112 250 156 526 92 L526 344 L0 344 Z" fill="#d9d9d9"/>
      <path d="M0 134 C120 118 250 162 526 98 L526 344 L0 344 Z" fill="#262626"/>
      <path d="M0 146 C130 130 260 170 526 110 L526 344 L0 344 Z" fill="url(#orangeFill)"/>
    </svg>

    <div class="brand">
      <div class="brand__row">
        <span class="brand__dot"></span>
        <span class="brand__name">Ventisca Home Health</span>
      </div>
      <span class="brand__tagline">Comfort Close to Home</span>
    </div>

    <div class="person">
      <p class="person__name">Tobias Quillmore</p>
      <p class="person__title">Administrator</p>
      <p class="person__address">4817 Linwood Rd. Suite 318<br>Brenmoor, Texas 70412</p>
      <p class="person__address">5400 Harlan Pruett<br>Calder Flats, Texas 70588</p>
    </div>

    <div class="divider"></div>

    <ul class="contacts">
      <li><svg viewBox="0 0 16 16"><path d="M4 1h3l1 4-2 1a8 8 0 0 0 4 4l1-2 4 1v3c0 1-1 2-2 2A13 13 0 0 1 2 3c0-1 1-2 2-2z" fill="#2b2b2b"/></svg>Brenmoor: 210-555-0147</li>
      <li><svg viewBox="0 0 16 16"><path d="M4 1h3l1 4-2 1a8 8 0 0 0 4 4l1-2 4 1v3c0 1-1 2-2 2A13 13 0 0 1 2 3c0-1 1-2 2-2z" fill="#2b2b2b"/></svg>Calder Flats: 915-555-0182</li>
      <li><svg viewBox="0 0 16 16"><rect x="4" y="1" width="8" height="14" rx="1.5" fill="#2b2b2b"/><rect x="5.5" y="3" width="5" height="8" fill="#fcc85a"/></svg>210-555-0163</li>
      <li><svg viewBox="0 0 16 16"><rect x="4" y="1" width="8" height="5" fill="#2b2b2b"/><rect x="1" y="6" width="14" height="7" rx="1" fill="#2b2b2b"/><rect x="4" y="11" width="8" height="4" fill="#fff"/></svg>1-866-555-0129</li>
      <li><svg viewBox="0 0 16 16"><text x="8" y="13" text-anchor="middle" font-size="15" font-weight="700" fill="#2b2b2b" font-family="PT Sans, sans-serif">@</text></svg>tobias@myventisca.example</li>
    </ul>
  </section>

  <section class="card card--back">
    <div class="back__mark">
      <span class="back__circle"></span>
      <span class="back__name">Ventisca Home Health</span>
    </div>
    <ul class="services">
      <li>Private Duty Nursing</li>
      <li>Speech Therapy</li>
      <li>Physical Therapy</li>
      <li>Occupational Therapy</li>
    </ul>
    <p class="website">www.myventisca.example</p>
  </section>
</body>
</html>
```